Venn Diagram Highlighting the Unique Value Proposition of eBrightHarbor

Objective: Visually represent how eBrightHarbor distinguishes itself from its competitors by integrating three key domains:
- Service
-Software Solutions
- Social and Environmental Impact.
Detailed Instructions:
General Design:
• Venn Diagram:
• Create a three-circle Venn diagram, with each circle representing one of the key domains.
• Ensure the circles overlap to show possible intersections between the three domains.
Circles:
• Titles:
• Circle 1: “Service”
• Circle 2: “Software Solutions”
• Circle 3: “Social and Environmental Impact”
• Colors:
• Apply distinct colors to each circle while maintaining a degree of transparency to clearly show overlapping zones.
Competitor Integration:
• Placement:
• Position icons or logos of different competitors around the diagram. For now, indicate each competitor such as:
• HAS
• B
• VS
•D
• E
• F
•G
• H
• I
• Connect each competitor to the appropriate part of the diagram
• For each competitor, include a short annotation indicating key information, such as raised funds.
eBrightHarbor Positioning:
• Place the logo or the name of eBrightHarbor at the center, where all three circles overlap, to illustrate its unique ability to integrate these three domains.
Legend:
• Create a clear and concise legend in one corner of the graphic to explain what each color or section represents.
Style and Aesthetics:
• Adopt a clean, professional design (We will provide the graphic charter later)
• Ensure the design is easily readable and understandable, avoiding overcrowding or any confusion.
Formats:
• Ensure the design is adaptable to various formats, especially for presentations, printed documents, and the web.
• Provide the final design in high-resolution PNG, JPEG, and an editable source file, such as PSD or AI.
Deadline: it is urgent
Target Market(s)
Investors
Industry/Entity Type
Impact-Tech Startup
Colors
Designer to choose colors to be used in the design.
Look and feel
Each slider illustrates characteristics of the customer's brand and the style your logo design should communicate.

```html
<!DOCTYPE html>
<html lang="en">
<head>
<meta charset="utf-8">
<title>eBrightHarbor – Value Proposition Venn Diagram</title>
<link href="https://fonts.googleapis.com/css2?family=Rubik:wght@400;500;600&display=swap" rel="stylesheet">
<style>
  :root {
    --red: #ec1c24;
    --green: #00a651;
    --navy: #2e3192;
    --salmon: #f0785a;
    --blush: #e9c4b6;
    --mint: #94d5aa;
    --leaf: #5fbe80;
    --lavender: #9d8fd3;
    --violet: #7e6cc0;
    --ink: #222222;
    --legend-orange: #f7a43b;
    --legend-blue: #1f78c8;
    --legend-green: #4cb85c;
  }
  html, body {
    margin: 0;
    padding: 0;
    width: 1200px;
    height: 900px;
    overflow: hidden;
    background: #ffffff;
  }
  .canvas {
    width: 1200px;
    height: 900px;
    display: block;
    font-family: "Rubik", sans-serif;
  }
  .brand-name { font-size: 28px; font-weight: 500; fill: var(--ink); }
  .domain-title { font-size: 21px; font-weight: 400; fill: #ffffff; text-anchor: middle; }
  .core-name { font-size: 8px; font-weight: 500; fill: #ffffff; text-anchor: middle; }
  .bubble-letter { font-weight: 500; fill: #ffffff; text-anchor: middle; dominant-baseline: central; }
  .note { font-size: 11.5px; font-weight: 500; fill: var(--ink); letter-spacing: 0.2px; }
  .note-left { text-anchor: end; }
  .connector { fill: none; stroke-width: 1; stroke-dasharray: 3 3; }
  .contact { font-size: 19px; font-weight: 500; fill: var(--ink); letter-spacing: 0.3px; }
  .blurb { font-size: 12.5px; fill: var(--ink); text-anchor: end; }
  .legend-copy { font-size: 12.5px; fill: var(--ink); }
  .legend-head { font-size: 12.5px; font-weight: 600; fill: var(--ink); }
  .legend-item { font-size: 11.5px; fill: var(--ink); }
</style>
</head>
<body>
<svg class="canvas" viewBox="0 0 1200 900" xmlns="http://www.w3.org/2000/svg">
  <defs>
    <radialGradient id="paperGlow" cx="50%" cy="45%" r="70%">
      <stop offset="0" stop-color="#ffffff"/>
      <stop offset="1" stop-color="#ececed"/>
    </radialGradient>
    <linearGradient id="legendFade" x1="0" y1="0" x2="0" y2="1">
      <stop offset="0" stop-color="#ffffff"/>
      <stop offset="1" stop-color="#f6f6f6"/>
    </linearGradient>
    <linearGradient id="redGreenBlend" gradientUnits="userSpaceOnUse" x1="546" y1="300" x2="656" y2="300">
      <stop offset="0" stop-color="#a8342a"/>
      <stop offset="0.5" stop-color="#7a6a35"/>
      <stop offset="1" stop-color="#2f8a48"/>
    </linearGradient>
    <linearGradient id="redNavyBlend" gradientUnits="userSpaceOnUse" x1="470" y1="390" x2="580" y2="480">
      <stop offset="0" stop-color="#b0283e"/>
      <stop offset="1" stop-color="#4a3590"/>
    </linearGradient>
    <linearGradient id="greenNavyBlend" gradientUnits="userSpaceOnUse" x1="730" y1="390" x2="630" y2="480">
      <stop offset="0" stop-color="#1a8a5a"/>
      <stop offset="1" stop-color="#25508c"/>
    </linearGradient>
    <linearGradient id="coreBlend" gradientUnits="userSpaceOnUse" x1="560" y1="385" x2="650" y2="440">
      <stop offset="0" stop-color="#c0303a"/>
      <stop offset="0.35" stop-color="#7a3a8a"/>
      <stop offset="0.65" stop-color="#3040a0"/>
      <stop offset="1" stop-color="#1a8a60"/>
    </linearGradient>
    <clipPath id="servicesClip"><circle cx="493" cy="327" r="163"/></clipPath>
    <clipPath id="softwareClip"><circle cx="709" cy="327" r="163"/></clipPath>
    <clipPath id="impactClip"><circle cx="608" cy="539" r="163"/></clipPath>
  </defs>

  <rect class="paper" width="1200" height="900" fill="url(#paperGlow)"/>

  <!-- Brand -->
  <g class="brand">
    <circle cx="98" cy="88" r="33" fill="var(--red)"/>
    <text class="brand-name" x="148" y="97">eBrightHarbor</text>
  </g>

  <!-- Connectors -->
  <g class="connectors">
    <path class="connector" stroke="var(--salmon)" d="M318 240 L345 262"/>
    <path class="connector" stroke="var(--red)" d="M269 303 L332 318"/>
    <path class="connector" stroke="var(--blush)" d="M303 388 L336 376"/>
    <path class="connector" stroke="var(--mint)" d="M836 176 L824 198"/>
    <path class="connector" stroke="var(--green)" d="M897 212 L850 246"/>
    <path class="connector" stroke="var(--leaf)" d="M902 290 L872 300"/>
    <path class="connector" stroke="var(--lavender)" d="M407 574 L442 563"/>
    <path class="connector" stroke="var(--violet)" d="M370 668 L460 620"/>
    <path class="connector" stroke="var(--navy)" d="M464 697 L496 658"/>
  </g>

  <!-- Venn -->
  <g class="venn">
    <circle class="domain-circle" cx="493" cy="327" r="163" fill="var(--red)"/>
    <circle class="domain-circle" cx="709" cy="327" r="163" fill="var(--green)"/>
    <circle class="domain-circle" cx="608" cy="539" r="163" fill="var(--navy)"/>
    <circle class="overlap" cx="709" cy="327" r="163" fill="url(#redGreenBlend)" clip-path="url(#servicesClip)"/>
    <circle class="overlap" cx="608" cy="539" r="163" fill="url(#redNavyBlend)" clip-path="url(#servicesClip)"/>
    <circle class="overlap" cx="608" cy="539" r="163" fill="url(#greenNavyBlend)" clip-path="url(#softwareClip)"/>
    <g clip-path="url(#servicesClip)">
      <circle class="overlap-core" cx="709" cy="327" r="163" fill="url(#coreBlend)" clip-path="url(#impactClip)"/>
    </g>
    <text class="core-name" x="603" y="405">eBrightHarbor</text>
  </g>

  <!-- Services -->
  <g class="domain services">
    <circle cx="447" cy="289" r="46" fill="#ffffff"/>
    <circle cx="438" cy="296" r="16" fill="none" stroke="var(--red)" stroke-width="7" stroke-dasharray="5 3.4"/>
    <circle cx="438" cy="296" r="5" fill="var(--red)"/>
    <circle cx="461" cy="276" r="10" fill="none" stroke="var(--red)" stroke-width="5" stroke-dasharray="3.5 2.8"/>
    <circle cx="467" cy="298" r="6" fill="none" stroke="var(--red)" stroke-width="4" stroke-dasharray="2.5 2"/>
    <text class="domain-title" x="446" y="366">Services</text>
  </g>

  <!-- Software Solutions -->
  <g class="domain software">
    <circle cx="754" cy="289" r="46" fill="#ffffff"/>
    <rect x="735" y="270" width="38" height="38" rx="8" fill="none" stroke="var(--green)" stroke-width="6"/>
    <path d="M744 289 L751 296 L764 282" fill="none" stroke="var(--green)" stroke-width="5" stroke-linecap="round" stroke-linejoin="round"/>
    <text class="domain-title" x="757" y="366">Software</text>
    <text class="domain-title" x="757" y="389">Solutions</text>
  </g>

  <!-- Social & Environmental Impact -->
  <g class="domain impact">
    <circle cx="606" cy="535" r="46" fill="#ffffff"/>
    <circle cx="606" cy="532" r="27" fill="var(--navy)" role="img" aria-label="Hands holding a globe icon"/>
    <text class="domain-title" x="607" y="614">Social And</text>
    <text class="domain-title" x="607" y="637">Environmental</text>
    <text class="domain-title" x="607" y="660">Impact</text>
  </g>

  <!-- Competitors -->
  <g class="competitor">
    <circle cx="302" cy="223" r="24" fill="var(--salmon)"/>
    <text class="bubble-letter" x="302" y="223" font-size="26">D</text>
    <text class="note note-left" x="267" y="220">INVESTMENT</text>
    <text class="note note-left" x="267" y="234">$1 MILLION</text>
  </g>
  <g class="competitor">
    <circle cx="230" cy="295" r="40" fill="var(--red)"/>
    <text class="bubble-letter" x="230" y="296" font-size="40">G</text>
    <text class="note note-left" x="177" y="296">INVESTMENT</text>
    <text class="note note-left" x="177" y="310">$1 MILLION</text>
  </g>
  <g class="competitor">
    <circle cx="275" cy="394" r="28" fill="var(--blush)"/>
    <text class="bubble-letter" x="275" y="395" font-size="30">C</text>
    <text class="note note-left" x="235" y="396">INVESTMENT</text>
    <text class="note note-left" x="235" y="410">$1 MILLION</text>
  </g>
  <g class="competitor">
    <circle cx="844" cy="152" r="26" fill="var(--mint)"/>
    <text class="bubble-letter" x="844" y="153" font-size="20">VS</text>
    <text class="note note-left" x="806" y="135">INVESTMENT</text>
    <text class="note note-left" x="806" y="150">$1.1 MILLION</text>
  </g>
  <g class="competitor">
    <circle cx="931" cy="184" r="38" fill="var(--green)"/>
    <text class="bubble-letter" x="931" y="185" font-size="21">HAS</text>
    <text class="note" x="981" y="174">INVESTMENT</text>
    <text class="note" x="981" y="189">$2.1 MILLION</text>
  </g>
  <g class="competitor">
    <circle cx="927" cy="287" r="26" fill="var(--leaf)"/>
    <text class="bubble-letter" x="927" y="288" font-size="24">F</text>
    <text class="note" x="965" y="282">INVESTMENT</text>
    <text class="note" x="965" y="297">$1.1 MILLION</text>
  </g>
  <g class="competitor">
    <circle cx="380" cy="579" r="27" fill="var(--lavender)"/>
    <text class="bubble-letter" x="380" y="580" font-size="28">B</text>
    <text class="note note-left" x="339" y="577">INVESTMENT</text>
    <text class="note note-left" x="339" y="591">$1.1 MILLION</text>
  </g>
  <g class="competitor">
    <circle cx="340" cy="680" r="31" fill="var(--violet)"/>
    <text class="bubble-letter" x="340" y="681" font-size="28">H</text>
    <text class="note note-left" x="296" y="679">INVESTMENT</text>
    <text class="note note-left" x="296" y="693">$2 MILLION</text>
  </g>
  <g class="competitor">
    <circle cx="436" cy="726" r="40" fill="var(--navy)"/>
    <text class="bubble-letter" x="436" y="727" font-size="42">E</text>
    <text class="note note-left" x="383" y="745">INVESTMENT</text>
    <text class="note note-left" x="383" y="759">$10 MILLION</text>
  </g>

  <!-- Legend -->
  <g class="legend">
    <rect x="920" y="554" width="205" height="310" fill="url(#legendFade)"/>
    <text class="legend-copy" x="946" y="591">Lorem ipsum dolor sit</text>
    <text class="legend-copy" x="946" y="607">amet, consectetuer</text>
    <text class="legend-copy" x="946" y="623">adipiscing elit, sed diam</text>
    <text class="legend-copy" x="946" y="639">nonummy nibh euismod</text>
    <text class="legend-copy" x="946" y="655">tincidunt ut laoreet</text>
    <text class="legend-copy" x="946" y="671">dolore magna aliquam</text>
    <text class="legend-copy" x="946" y="687">erat volutpat. Ut wisi enim</text>
    <text class="legend-head" x="948" y="723">INFORMATION</text>
    <circle cx="955" cy="762" r="8" fill="var(--legend-orange)"/>
    <text class="legend-item" x="970" y="758">Social and</text>
    <text class="legend-item" x="970" y="773">Environmental Impact</text>
    <circle cx="955" cy="804" r="8" fill="var(--legend-blue)"/>
    <text class="legend-item" x="970" y="800">Software</text>
    <text class="legend-item" x="970" y="815">Solutions</text>
    <circle cx="955" cy="838" r="8" fill="var(--legend-green)"/>
    <text class="legend-item" x="970" y="842">Services</text>
  </g>

  <!-- Footer -->
  <g class="footer">
    <text class="contact" x="62" y="860">014 555 20918  |  WWW.EBRIGHTHARBOR.COM</text>
    <text class="blurb" x="896" y="829">Lorem ipsum dolor sit amet, consectetuer adipiscing elit,</text>
    <text class="blurb" x="896" y="845">sed diam nonummy nibh euismod tincidunt ut laoreet dolore</text>
    <text class="blurb" x="896" y="861">magna aliquam erat volutpat. Ut wisi enim</text>
  </g>
</svg>
</body>
</html>
```